Poster for pawn shop lobby

Looking for green and gold as my colors, like the picture shown of my old poster. This time I'm contemplating with doing pictures as well as just text. Here are ideas of things I buy and give loans on. We want to emphasize jewelry, laptops, game systems, tools. I'm open-minded.
Old & Broken Gold
Jewelry & Collectibles
Diamonds
Video Games & Systems
Up-to-date Computers & Laptops
Tablets
Cameras
Power Tools
Home & Garden Equipment
Sports Equipment
Watches
Antique Collectibles
Musical Instruments
And anything else of value
Shop

```html
<!DOCTYPE html>
<html lang="en">
<head>
<meta charset="utf-8">
<title>We'll Loan or Pay You On — Pawn Shop Lobby Poster</title>
<link rel="stylesheet" href="https://fonts.googleapis.com/css2?family=Archivo:wght@700;800&family=PT+Sans:wght@400;700&display=swap">
<style>
  :root {
    --parchment-light: #e9e6d6;
    --parchment-mid: #d4cfb6;
    --parchment-dark: #b9b295;
    --gold: #c4921b;
    --leaf-green: #6b9a2b;
    --forest-green: #2d5a36;
    --ink: #111111;
    --white: #ffffff;
    --divider: #6b5a2a;
  }
  * { box-sizing: border-box; margin: 0; padding: 0; }
  html, body { width: 903px; height: 1200px; overflow: hidden; }
  body {
    position: relative;
    background: radial-gradient(ellipse at 50% 45%, var(--parchment-light) 0%, var(--parchment-mid) 60%, var(--parchment-dark) 100%);
    font-family: "PT Sans", Arial, sans-serif;
  }
  .poster {
    position: absolute;
    left: 76px; top: 79px;
    width: 744px; height: 1028px;
    background: var(--gold);
  }
  .headline {
    height: 185px;
    background: var(--leaf-green);
    color: var(--forest-green);
    font-family: "Archivo", Arial, sans-serif;
    font-weight: 800;
    font-size: 88px;
    line-height: 80px;
    text-align: center;
    padding-top: 16px;
    letter-spacing: 0;
  }
  .featured {
    color: var(--ink);
    font-family: "Archivo", Arial, sans-serif;
    font-weight: 700;
    font-size: 49px;
    line-height: 68px;
    text-align: center;
    padding-top: 0;
  }
  .featured span { margin: 0 12px; }
  .column-divider {
    position: absolute;
    left: 395px; top: 331px;
    width: 2px; height: 688px;
    background: var(--divider);
  }
  .category { position: absolute; width: 340px; }
  .category-title {
    color: var(--forest-green);
    font-weight: 700;
    font-size: 19.5px;
    line-height: 28px;
    text-transform: uppercase;
    letter-spacing: 0.1px;
  }
  .item-list { list-style: none; }
  .item-list li {
    color: var(--white);
    font-size: 21.5px;
    line-height: 28.5px;
    padding-left: 14px;
    text-indent: -14px;
  }
  .item-list li::before { content: "•"; display: inline-block; width: 14px; text-indent: 0; }
  .thumb { position: absolute; }
</style>
</head>
<body>
  <main class="poster">
    <header class="headline">We’ll LOAN or<br>pay you $$$$ on</header>
    <div class="featured">
      <span>$Jewelry</span><span>$Laptops</span><span>$Tools</span><br>
      <span>$Game Systems</span>
    </div>

    <div class="column-divider"></div>

    <section class="category" style="left:25px; top:325px;">
      <h2 class="category-title">Sporting Equipment &amp; Vehicles</h2>
      <ul class="item-list">
        <li>Sports Equipment</li><li>Motorcycles</li><li>Snowmobiles</li><li>Golf Clubs</li><li>Bicycles</li>
      </ul>
    </section>
    <section class="category" style="left:25px; top:511px;">
      <h2 class="category-title">Home Improvement</h2>
      <ul class="item-list">
        <li>Power Tools</li><li>Home &amp; Garden Equipment</li><li>Lawn Mowers</li><li>Leaf Blowers</li><li>Snow Blowers</li>
      </ul>
    </section>
    <section class="category" style="left:25px; top:692px;">
      <h2 class="category-title">Miscellaneous</h2>
      <ul class="item-list">
        <li>Microwave Ovens</li><li>Small Home Applianes</li><li>Quality Leather</li><li>Artwork</li>
      </ul>
    </section>
    <section class="category" style="left:25px; top:843px;">
      <h2 class="category-title">Musical Instruments</h2>
      <ul class="item-list">
        <li>Guitars</li><li>Band Instruments</li><li>Amplifiers</li><li>DJ Equipment</li>
      </ul>
    </section>

    <section class="category" style="left:416px; top:326px;">
      <h2 class="category-title">Video Games &amp; Computers</h2>
      <ul class="item-list">
        <li>Video Games &amp; Systems</li><li>Up-to-date ComputersLaptos</li><li>Tablets</li><li>Monitors &amp; Accessories</li><li>Compact Discs</li>
      </ul>
    </section>
    <section class="category" style="left:416px; top:506px;">
      <h2 class="category-title">Audio &amp; Video</h2>
      <ul class="item-list">
        <li>Car Audio</li><li>Home Audio Systems</li><li>Speakers</li><li>Televisions</li><li>Home Theater Systems</li><li>Functioning Electronic Devices</li>
      </ul>
    </section>
    <section class="category" style="left:416px; top:746px;">
      <h2 class="category-title">Jewelry &amp; Collectibles</h2>
      <ul class="item-list">
        <li>Diamond &amp; Gemstone Jewelry</li><li>Watches</li><li>Old &amp; Broken Gold</li><li>Antique Collectibles</li>
      </ul>
    </section>
    <section class="category" style="left:416px; top:925px;">
      <h2 class="category-title">DVD &amp; Blu-Ray Movies</h2>
      <ul class="item-list">
        <li>DVD Movies</li><li>Blu-Ray Movies</li>
      </ul>
    </section>

    <svg class="thumb" style="left:291px; top:393px;" width="87" height="60" role="img" aria-label="Collage of colourful sports pictures">
      <defs><linearGradient id="g-sport" x1="0" y1="0" x2="1" y2="1"><stop offset="0" stop-color="#d8402e"/><stop offset="0.5" stop-color="#3a78c4"/><stop offset="1" stop-color="#e7b83a"/></linearGradient></defs>
      <rect width="87" height="60" fill="url(#g-sport)"/>
    </svg>
    <svg class="thumb" style="left:291px; top:600px;" width="87" height="60" role="img" aria-label="Photo of a couple planning a home improvement project">
      <defs><linearGradient id="g-home" x1="0" y1="0" x2="1" y2="1"><stop offset="0" stop-color="#c9c4b8"/><stop offset="1" stop-color="#6d5a44"/></linearGradient></defs>
      <rect width="87" height="60" fill="url(#g-home)"/>
    </svg>
    <svg class="thumb" style="left:307px; top:749px;" width="70" height="64" role="img" aria-label="Colourful circular wheel illustration">
      <defs><radialGradient id="g-wheel"><stop offset="0.3" stop-color="#ffffff"/><stop offset="0.6" stop-color="#e8a030"/><stop offset="1" stop-color="#4a8ad0"/></radialGradient></defs>
      <rect width="70" height="64" fill="#ffffff"/><circle cx="35" cy="32" r="26" fill="url(#g-wheel)"/>
    </svg>
    <svg class="thumb" style="left:291px; top:897px;" width="86" height="58" role="img" aria-label="Photo of hands playing a guitar">
      <defs><linearGradient id="g-music" x1="0" y1="0" x2="1" y2="1"><stop offset="0" stop-color="#2a1e18"/><stop offset="1" stop-color="#b0703a"/></linearGradient></defs>
      <rect width="86" height="58" fill="url(#g-music)"/>
    </svg>
    <svg class="thumb" style="left:663px; top:422px;" width="65" height="83" role="img" aria-label="Photo of two friends playing video games">
      <defs><linearGradient id="g-games" x1="0" y1="0" x2="1" y2="1"><stop offset="0" stop-color="#d9d6cf"/><stop offset="1" stop-color="#4a6b4a"/></linearGradient></defs>
      <rect width="65" height="83" fill="url(#g-games)"/>
    </svg>
    <svg class="thumb" style="left:642px; top:600px;" width="86" height="57" role="img" aria-label="Photo of a person relaxing with headphones">
      <defs><linearGradient id="g-audio" x1="0" y1="0" x2="1" y2="0"><stop offset="0" stop-color="#f4f4f4"/><stop offset="1" stop-color="#c8b8a8"/></linearGradient></defs>
      <rect width="86" height="57" fill="url(#g-audio)"/>
    </svg>
    <svg class="thumb" style="left:642px; top:818px;" width="86" height="57" role="img" aria-label="Photo of gold chains and jewelry">
      <defs><linearGradient id="g-gold" x1="0" y1="0" x2="1" y2="1"><stop offset="0" stop-color="#f6f2e8"/><stop offset="0.5" stop-color="#c89a3a"/><stop offset="1" stop-color="#f2ece0"/></linearGradient></defs>
      <rect width="86" height="57" fill="url(#g-gold)"/>
    </svg>
    <svg class="thumb" style="left:652px; top:939px;" width="76" height="67" role="img" aria-label="Photo of a television showing a movie">
      <defs><radialGradient id="g-tv"><stop offset="0" stop-color="#8ab0d8"/><stop offset="1" stop-color="#0c1420"/></radialGradient></defs>
      <rect width="76" height="67" fill="url(#g-tv)"/>
    </svg>
  </main>
</body>
</html>
```